Need Icons design for timeline

We want to use a timeline component (http://chronoline.example-plume.net/) to show business synergy history. Our business is petrochemical and refinery.

We need the following images.
1. Icon: Business Development (BD) - size 30x30 px
2. Icon: Merger and Acquisition (MA) - size 30x30 px
3. Icon: Synergy - size 30x30 px
4. Image for Timeline progress as attached. Width = 700px
4.1 Show Year for each progress
4.2 Has indicator showing the active progress or highlight the active progress
4.3 There are 3 progresses
- Facing Financial Crisis
- Huge New Capacity & Economic Downturn
- Global Competition

Reason: Customer provides more detail as updated in the Must have features section.

Industry/Entity Type

Business

Requirements
Must have
• 1. All 3 icons must have white (transparent background) without border.
2. "Business Development" icon should use picture that represents business growth. For example, a rising chart.
3. "Merger and Acquisition" icon should use picture that represents two parties agreeing on something. For example, two people shaking hands.
4. "Synergy" icon should use picture that represents small parts forming a big picture. For example, jigsaw.
5. There should not be too much detail on the icons because they will be resized to 30x30 pixels.

```html
<!DOCTYPE html>
<html lang="en">
<head>
<meta charset="utf-8">
<title>Synergy Timeline Icons</title>
<link href="https://fonts.googleapis.com/css2?family=Open+Sans:wght@400;600;700&display=swap" rel="stylesheet">
<style>
  :root {
    --ink: #2b2b2b;
    --label: #3a3a3a;
    --muted: #9a9a9a;
    --year: #a6a6a6;
    --bar-top: #ffffff;
    --bar-bottom: #ececec;
    --bar-edge: #c9c9c9;
    --active-top: #43a6ee;
    --active-bottom: #1c7bd6;
    --white: #ffffff;
    --page: #ffffff;
  }
  html, body {
    margin: 0;
    padding: 0;
    width: 1200px;
    height: 525px;
    overflow: hidden;
    background: var(--page);
    font-family: "Open Sans", Arial, sans-serif;
  }
  .canvas {
    position: relative;
    width: 1200px;
    height: 525px;
  }
  .icon-set { position: absolute; inset: 0; }
  .icon {
    position: absolute;
    text-align: center;
  }
  .icon svg { display: block; margin: 0 auto; }
  .icon-label {
    margin: 0;
    font-size: 22px;
    line-height: 26px;
    color: var(--label);
  }
  .icon--bd { left: 271px; top: 54px; width: 180px; }
  .icon--bd .icon-label { margin-top: 40px; }
  .icon--ma { left: 492px; top: 52px; width: 180px; }
  .icon--ma .icon-label { margin-top: 22px; }
  .icon--synergy { left: 700px; top: 56px; width: 180px; }
  .icon--synergy .icon-label { margin-top: 26px; }

  .timeline {
    position: absolute;
    left: 85px;
    top: 348px;
    width: 1022px;
    height: 74px;
    border: 1px solid var(--bar-edge);
    border-radius: 4px;
    background: linear-gradient(var(--bar-top), var(--bar-bottom));
    box-sizing: border-box;
  }
  .stage {
    position: absolute;
    top: 0;
    height: 72px;
    display: flex;
    align-items: center;
    font-size: 22px;
    line-height: 25px;
    color: var(--muted);
  }
  .stage svg { flex: none; margin-right: 14px; }
  .stage--active {
    left: -1px;
    top: -1px;
    height: 74px;
    width: 342px;
    padding-left: 24px;
    box-sizing: border-box;
    color: var(--white);
    background: linear-gradient(var(--active-top), var(--active-bottom));
    border-radius: 4px 0 0 4px;
    clip-path: polygon(0 0, 318px 0, 342px 50%, 318px 100%, 0 100%);
  }
  .stage--capacity { left: 362px; }
  .stage--global { left: 700px; }
  .chevron { position: absolute; left: 665px; top: 20px; }

  .year {
    position: absolute;
    top: 437px;
    margin: 0;
    font-size: 26px;
    font-weight: 700;
    color: var(--year);
  }
  .year--2009 { left: 361px; }
  .year--2011 { left: 712px; }
</style>
</head>
<body>
<div class="canvas">
  <section class="icon-set">
    <figure class="icon icon--bd" style="margin:0">
      <svg width="98" height="98" viewBox="0 0 98 98" aria-hidden="true">
        <rect x="46" y="2" width="6" height="8" fill="var(--ink)"/>
        <rect x="6" y="10" width="86" height="64" rx="3" fill="var(--ink)"/>
        <polyline points="18,58 36,40 48,50 72,26" fill="none" stroke="var(--white)" stroke-width="6" stroke-linejoin="round"/>
        <polygon points="62,22 80,18 76,36" fill="var(--white)"/>
        <rect x="16" y="74" width="7" height="22" fill="var(--ink)"/>
        <rect x="75" y="74" width="7" height="22" fill="var(--ink)"/>
        <rect x="2" y="78" width="94" height="7" fill="var(--ink)"/>
      </svg>
      <figcaption class="icon-label">Business<br>Development</figcaption>
    </figure>

    <figure class="icon icon--ma" style="margin:0">
      <svg width="134" height="122" viewBox="0 0 134 122" aria-hidden="true">
        <path d="M67 112 L14 60 C-4 40 8 6 36 6 C50 6 60 14 67 24 C74 14 84 6 98 6 C126 6 138 40 120 60 Z" fill="none" stroke="var(--ink)" stroke-width="6" stroke-linejoin="round"/>
        <path d="M20 52 L46 32 L62 38 L44 50 C40 54 46 60 52 56 L70 44 L104 66 C108 70 104 76 98 72 C102 78 96 82 92 78 C94 84 88 86 84 82 C84 88 78 88 74 84 L66 90 L22 58 Z" fill="var(--white)" stroke="var(--ink)" stroke-width="5" stroke-linejoin="round"/>
        <path d="M114 52 L92 34 L74 36 L52 52" fill="none" stroke="var(--ink)" stroke-width="5" stroke-linejoin="round"/>
      </svg>
      <figcaption class="icon-label">Merger &amp;<br>Acquisition</figcaption>
    </figure>

    <figure class="icon icon--synergy" style="margin:0">
      <svg width="130" height="116" viewBox="0 0 130 116" aria-hidden="true">
        <g fill="var(--ink)">
          <rect x="20" y="4" width="50" height="50"/>
          <rect x="74" y="4" width="50" height="50"/>
          <rect x="20" y="58" width="50" height="50"/>
          <rect x="74" y="58" width="50" height="50"/>
          <circle cx="72" cy="29" r="9"/>
          <circle cx="45" cy="56" r="9"/>
          <circle cx="99" cy="56" r="9"/>
          <circle cx="72" cy="83" r="9"/>
          <circle cx="14" cy="83" r="9"/>
        </g>
        <g fill="var(--white)">
          <circle cx="20" cy="29" r="8"/>
          <circle cx="124" cy="83" r="8"/>
        </g>
      </svg>
      <figcaption class="icon-label">Synergy</figcaption>
    </figure>
  </section>

  <nav class="timeline" aria-label="Synergy history progress">
    <div class="stage stage--active">
      <svg width="30" height="30" viewBox="0 0 30 30" aria-hidden="true">
        <g fill="none" stroke="var(--white)" stroke-width="2">
          <polyline points="3,2 3,27 28,27"/>
        </g>
        <g fill="var(--white)">
          <rect x="7" y="8" width="4" height="16"/>
          <rect x="14" y="13" width="4" height="11"/>
          <rect x="21" y="17" width="4" height="7"/>
        </g>
      </svg>
      Facing Financial Crisis
    </div>
    <div class="stage stage--capacity">
      <svg width="30" height="30" viewBox="0 0 30 30" aria-hidden="true">
        <g fill="none" stroke="var(--muted)" stroke-width="2">
          <polyline points="3,2 3,27 28,27"/>
          <polyline points="7,18 13,11 18,15 26,6"/>
        </g>
        <g fill="var(--muted)">
          <rect x="7" y="20" width="4" height="5"/>
          <rect x="14" y="18" width="4" height="7"/>
          <rect x="21" y="14" width="4" height="11"/>
        </g>
      </svg>
      Huge New Capacity &amp;<br>Economic Downturn
    </div>
    <svg class="chevron" width="16" height="34" viewBox="0 0 16 34" aria-hidden="true">
      <polyline points="2,1 14,17 2,33" fill="none" stroke="var(--bar-edge)" stroke-width="1.5"/>
    </svg>
    <div class="stage stage--global">
      <svg width="32" height="32" viewBox="0 0 32 32" aria-hidden="true">
        <g fill="none" stroke="var(--muted)" stroke-width="2">
          <circle cx="16" cy="16" r="14"/>
          <ellipse cx="16" cy="16" rx="6" ry="14"/>
          <line x1="2" y1="16" x2="30" y2="16"/>
          <line x1="4" y1="9" x2="28" y2="9"/>
          <line x1="4" y1="23" x2="28" y2="23"/>
          <line x1="16" y1="2" x2="16" y2="30"/>
        </g>
      </svg>
      Global Competition
    </div>
  </nav>

  <p class="year year--2009">2009</p>
  <p class="year year--2011">2011</p>
</div>
</body>
</html>
```